Bright Lantern Way (BLWY) Business Card - company with a mission

Note* The file attached... orange with "Bright Lantern WAY" (in CAPS) is our logo. I am also open to having the text "bright lantern way" OUTSIDE the orange round logo for business card (so yes, you may take the text out).

The info: (the following info are separate. So either you can use Marcus or Renata for now, but that will be 2 separate cards, not together in one card. Thanks!!

Marcus T Delvin
202.555.0137
marcus@brightlanternway.example
Managing Partner

Renata P Osk
202.555.0184
renata@brightlanternway.example
Managing Partner

Our website: www.brightlanternway.example

BLWY LLC stands for Bright Lantern Way (non profit arm is called lantern glow foundation)—our business is based out of New York City and has a non-profit arm where for every bar of soap you purchase, we donate a bar (don’t want any designs that limits us to only soap). Currently working with South Africa. We want the focus to be organic/natural soap with a mission.

Looking for a clean, fresh design.

Industry/Entity Type

Non-Profit

Requirements
Must have
• Clean, fresh, refreshing. Design should not be too busy.

```html
<!DOCTYPE html>
<html lang="en">
<head>
<meta charset="utf-8">
<title>Bright Lantern Way – Business Card</title>
<link href="https://fonts.googleapis.com/css2?family=Lato:wght@300;400;700;900&display=swap" rel="stylesheet">
<style>
  :root {
    --backdrop: #3b3b3d;
    --card-edge: #ffffff;
    --card-face: #f3ae6c;
    --ink: #121212;
    --ink-soft: #2b2b2b;
    --seal: #3f3e3e;
    --seal-text: #ffffff;
    --rule: #6b4a2c;
  }
  * { box-sizing: border-box; margin: 0; padding: 0; }
  html, body {
    width: 1200px;
    height: 926px;
    overflow: hidden;
    background: var(--backdrop);
    font-family: "Lato", sans-serif;
  }
  .stage {
    position: relative;
    width: 1200px;
    height: 926px;
  }
  .card {
    position: absolute;
    left: 290px;
    width: 620px;
    height: 354px;
    background: var(--card-edge);
    padding: 14px;
    box-shadow: 0 6px 18px rgba(0,0,0,.35);
  }
  .card--back { top: 70px; }
  .card--front { top: 480px; }
  .card__face {
    position: relative;
    width: 100%;
    height: 100%;
    background: var(--card-face);
  }

  /* Back: brand seal */
  .brand-seal {
    position: absolute;
    left: 50%;
    top: 50%;
    width: 180px;
    height: 180px;
    margin: -90px 0 0 -90px;
    border-radius: 50%;
    background: var(--seal);
    display: flex;
    align-items: center;
    justify-content: center;
    text-align: center;
  }
  .brand-seal__name {
    color: var(--seal-text);
    font-weight: 700;
    font-size: 22px;
    line-height: 1.15;
    letter-spacing: .5px;
  }

  /* Front: identity */
  .identity {
    position: absolute;
    left: 66px;
    top: 84px;
  }
  .identity__name {
    font-size: 36px;
    color: var(--ink);
    letter-spacing: .5px;
    line-height: 1;
  }
  .identity__first { font-weight: 300; }
  .identity__last { font-weight: 700; }
  .identity__role {
    margin: 10px 0 0 120px;
    font-size: 15px;
    font-weight: 400;
    letter-spacing: 2.4px;
    color: var(--ink-soft);
  }

  .contact-row {
    position: absolute;
    left: 14px;
    right: 14px;
    bottom: 22px;
    display: flex;
    gap: 14px;
  }
  .contact {
    display: flex;
    flex-direction: column;
    align-items: center;
  }
  .contact--phone { width: 110px; }
  .contact--web { width: 190px; }
  .contact--mail { flex: 1; }
  .contact__icon {
    width: 26px;
    height: 26px;
    border-radius: 50%;
    background: var(--ink);
    display: flex;
    align-items: center;
    justify-content: center;
  }
  .contact__icon svg { width: 14px; height: 14px; }
  .contact__rule {
    width: 100%;
    height: 1px;
    margin: 8px 0 10px;
    background: var(--rule);
  }
  .contact__text {
    font-size: 12.5px;
    font-weight: 700;
    color: var(--ink);
    white-space: nowrap;
    letter-spacing: .2px;
  }
  .contact__sep { font-weight: 700; margin-left: 6px; }
</style>
</head>
<body>
<main class="stage">

  <section class="card card--back" aria-label="Business card back">
    <div class="card__face">
      <div class="brand-seal">
        <p class="brand-seal__name">Bright<br>Lantern<br>Way</p>
      </div>
    </div>
  </section>

  <section class="card card--front" aria-label="Business card front">
    <div class="card__face">
      <div class="identity">
        <h1 class="identity__name"><span class="identity__first">MARCUS</span> <span class="identity__last">T DELVIN</span></h1>
        <p class="identity__role">MANAGING PARTNER</p>
      </div>

      <div class="contact-row">
        <div class="contact contact--phone">
          <span class="contact__icon">
            <svg viewBox="0 0 16 16" aria-hidden="true"><rect x="2" y="4" width="12" height="8" fill="none" stroke="#f3ae6c" stroke-width="1.4"/><path d="M2 4l6 5 6-5" fill="none" stroke="#f3ae6c" stroke-width="1.4"/></svg>
          </span>
          <span class="contact__rule"></span>
          <span class="contact__text">202.555.0137<span class="contact__sep">|</span></span>
        </div>
        <div class="contact contact--web">
          <span class="contact__icon">
            <svg viewBox="0 0 16 16" aria-hidden="true"><rect x="2" y="3" width="12" height="8" fill="none" stroke="#f3ae6c" stroke-width="1.4"/><path d="M8 11v2M5 13.5h6" stroke="#f3ae6c" stroke-width="1.4"/></svg>
          </span>
          <span class="contact__rule"></span>
          <span class="contact__text">www.brightlanternway.example<span class="contact__sep">|</span></span>
        </div>
        <div class="contact contact--mail">
          <span class="contact__icon">
            <svg viewBox="0 0 16 16" aria-hidden="true"><path d="M2 6c0-2 12-2 12 0v1h-3V6H5v1H2z" fill="#f3ae6c"/><rect x="4" y="8" width="8" height="5" rx="1" fill="#f3ae6c"/><circle cx="8" cy="10.5" r="1.2" fill="#121212"/></svg>
          </span>
          <span class="contact__rule"></span>
          <span class="contact__text">marcus@brightlanternway.example</span>
        </div>
      </div>
    </div>
  </section>

</main>
</body>
</html>
```